Résumé app needs 1 more template

Hi, I need 1 more template for my résumé app. The résumé app can be used in a browser (https://pagekilnworks.com/resume-app) on an Zelvo / Zelvo Tab (https://apps.velmoro.net/app/id552817306) or on an Brevix (https://store.quintrel.net/store/apps/details?id=com.pagekilnworks.resume). The app lets the user create a résumé. It currently let's the user choose between 3 templates. I need 1 more. Please use the app first so you know how it will work.

Target Market(s)

Users of the app

Colors

Designer to choose colors to be used in the design.

Requirements
Must have
• original
• beautiful
• the resume template contains the data that the user can currently enter in the app (so do NOT design new features like sliders for level of experience etc)

```html
<!DOCTYPE html>
<html lang="en">
<head>
<meta charset="utf-8">
<title>Résumé Template</title>
<link rel="stylesheet" href="https://fonts.googleapis.com/css2?family=Montserrat:wght@300;400;500;600&display=swap">
<style>
  :root {
    --navy: #0d2b45;
    --navy-deep: #061522;
    --ink: #0c2c48;
    --cyan: #00b3cb;
    --cyan-soft: #a9dde3;
    --mist: #e9edf0;
    --text: #6b6b6b;
    --block: #6e6e6e;
    --white: #ffffff;
  }
  * { margin: 0; padding: 0; box-sizing: border-box; }
  html, body { width: 927px; height: 1200px; overflow: hidden; background: var(--white); }
  body { font-family: "Montserrat", Arial, sans-serif; color: var(--text); }
  .resume { position: relative; width: 927px; height: 1200px; overflow: hidden; }
  .backdrop { position: absolute; inset: 0; }
  .portrait {
    position: absolute; left: 28px; top: 28px; width: 272px; height: 272px;
    border-radius: 50%; background: var(--white); border: 2px solid var(--navy);
    display: flex; align-items: center; justify-content: center;
  }
  .portrait-fill { width: 232px; height: 232px; border-radius: 50%; background: linear-gradient(#eeeeee, #e2e2e2); }
  .identity { position: absolute; right: 55px; top: 44px; text-align: right; color: var(--white); }
  .name { font-size: 58px; font-weight: 500; line-height: 1; letter-spacing: 0.5px; }
  .designation { font-size: 29px; font-weight: 300; margin-top: 12px; letter-spacing: 0.5px; }
  .contact { position: absolute; right: 55px; top: 186px; text-align: right; color: var(--white);
    font-size: 18px; font-weight: 500; line-height: 34.5px; list-style: none; letter-spacing: -0.3px; }
  .intro { position: absolute; left: 28px; top: 336px; width: 440px; font-size: 17.5px; font-weight: 300; line-height: 24px; letter-spacing: 0.3px; }
  .intro p + p { margin-top: 15px; }
  .section-title { color: var(--ink); font-size: 28px; font-weight: 500; letter-spacing: 0.5px; line-height: 1; }
  .column { position: absolute; top: 605px; width: 380px; }
  .column-experience { left: 28px; }
  .column-education { left: 510px; }
  .entry-name { font-size: 20px; font-weight: 300; margin-top: 22px; letter-spacing: 0.3px; }
  .entry-years { font-size: 20px; font-weight: 300; margin-top: 17px; letter-spacing: 0.5px; }
  .entry-text { font-size: 17.5px; font-weight: 300; line-height: 24px; margin-top: 16px; width: 360px; letter-spacing: 0.3px; }
  .entry-mark { position: absolute; top: 1px; left: 290px; width: 85px; height: 85px; background: var(--block); }
  .divider { position: absolute; left: 456px; top: 606px; width: 4px; height: 308px;
    background: linear-gradient(to bottom, rgba(0,0,0,0), rgba(0,0,0,0.12) 30%, rgba(0,0,0,0.12) 70%, rgba(0,0,0,0)); filter: blur(1.5px); }
  .other { position: absolute; left: 28px; top: 935px; width: 865px; }
  .other-text { font-size: 17.5px; font-weight: 300; line-height: 21px; margin-top: 14px; letter-spacing: 0.3px; }
  .other-text p + p { margin-top: 15px; }
</style>
</head>
<body>
<main class="resume">
  <svg class="backdrop" width="927" height="1200" viewBox="0 0 1159 1500" aria-hidden="true">
    <polygon points="0,0 1159,0 1159,485 690,472 600,300 560,183 0,172" fill="var(--navy)"/>
    <polygon points="560,183 680,0 1159,0 1159,175 760,250" fill="var(--navy-deep)"/>
    <polygon points="0,200 370,214 560,183 600,268 360,268 0,232" fill="var(--cyan)"/>
    <polygon points="360,268 600,268 612,302 385,302" fill="var(--cyan-soft)"/>
    <polygon points="0,232 360,268 612,302 648,395 0,262" fill="var(--mist)"/>
    <polygon points="690,472 1159,485 1159,610 960,560" fill="var(--cyan)"/>
    <polygon points="700,480 960,560 1159,610 1159,705" fill="var(--cyan-soft)"/>
    <defs>
      <linearGradient id="footFade" x1="0" y1="0" x2="0" y2="1">
        <stop offset="0" stop-color="#ffffff"/>
        <stop offset="1" stop-color="#bfe6ec"/>
      </linearGradient>
    </defs>
    <rect x="0" y="1400" width="1159" height="82" fill="url(#footFade)"/>
    <rect x="0" y="1482" width="1159" height="18" fill="var(--navy)"/>
  </svg>

  <div class="portrait"><div class="portrait-fill" role="img" aria-label="Profile photo placeholder"></div></div>

  <header class="identity">
    <h1 class="name">Your Name</h1>
    <p class="designation">Designation</p>
  </header>
  <ul class="contact">
    <li>Street</li>
    <li>Postal Code</li>
    <li>City 000000</li>
    <li>0000 0000</li>
    <li>abc@xmail.com</li>
  </ul>

  <section class="intro">
    <p>Lorem Ipsum dummy texts was available for many years on adhesive sheets in different sizes and typefaces from a company called Tremavo.</p>
    <p>When computers came along, Orvel included lorem ipsum in its SheetSmith publishing software, and you now see it wherever designers, content designers, art directors, user interface developers and web designer are at work.</p>
  </section>

  <section class="column column-experience">
    <h2 class="section-title">EXPERIENCE</h2>
    <div class="entry-mark"></div>
    <p class="entry-name">Company Name</p>
    <p class="entry-years">2000-0000</p>
    <p class="entry-text">When computers came along, Orvel included lorem ipsum in its SheetSmith publishing software, and you now see it wherever designers, content designers, art directors, user interface developers and web designer are at work.</p>
  </section>

  <div class="divider"></div>

  <section class="column column-education">
    <h2 class="section-title">EDUCATION</h2>
    <div class="entry-mark"></div>
    <p class="entry-name">School Name</p>
    <p class="entry-years">2000-0000</p>
    <p class="entry-text">When computers came along, Orvel included lorem ipsum in its SheetSmith publishing software, and you now see it wherever designers, content designers, art directors, user interface developers and web designer are at work.</p>
  </section>

  <section class="other">
    <h2 class="section-title">OTHER</h2>
    <div class="other-text">
      <p>Lorem Ipsum dummy texts was available for many years on adhesive sheets in different sizes and typefaces from a company called Tremavo.</p>
      <p>When computers came along, Orvel included lorem ipsum in its SheetSmith publishing software, and you now see it wherever designers, content designers, art directors, user interface developers and web designer are at work.</p>
    </div>
  </section>
</main>
</body>
</html>
```